Need a professional card design. Marlowe building company specialise in residential and commercial builds. New homes, additions & renovations.
Wanting a card with creativity and professionalism.
Want card that utilises logo.

Back and front.

I have just created a logo, and want to use it on the business card.
Attached a copy of the logo.
Attached is also a current business card which I wish to redesign

please utilise both sides

• Reg# 38095

```html
<!DOCTYPE html>
<html lang="en">
<head>
<meta charset="utf-8">
<title>Marlowe Building Co — Business Card</title>
<link rel="stylesheet" href="https://fonts.googleapis.com/css2?family=Jost:wght@400;500;600&display=swap">
<style>
  :root {
    --bg: #d9d9d9;
    --card-white: #f7f7f6;
    --card-dark: #2a2625;
    --ink: #232021;
    --ink-soft: #4a4647;
    --gold: #e0a232;
    --light: #ecebea;
  }
  * { box-sizing: border-box; margin: 0; padding: 0; }
  html, body { width: 1200px; height: 961px; overflow: hidden; }
  body {
    background: var(--bg);
    font-family: "Jost", sans-serif;
    display: flex;
    align-items: center;
    justify-content: center;
    gap: 40px;
  }
  .card {
    position: relative;
    width: 520px;
    height: 290px;
    border-radius: 22px;
    overflow: hidden;
  }

  /* Front */
  .card-front { background: var(--card-white); color: var(--ink); }
  .card-front .brand {
    position: absolute; left: 40px; top: 92px;
    display: flex; align-items: center; gap: 10px;
  }
  .brand-mark { width: 14px; height: 14px; background: var(--gold); }
  .brand-name {
    font-weight: 500; font-size: 24px; letter-spacing: 1px;
    text-transform: uppercase; color: var(--ink);
  }
  .person { position: absolute; left: 40px; top: 200px; }
  .person-name { font-weight: 600; font-size: 15px; letter-spacing: 1px; }
  .person-role { font-size: 12px; color: var(--ink-soft); }
  .contact-address {
    position: absolute; right: 40px; top: 40px;
    font-size: 12px; line-height: 1.4; text-align: right; color: var(--ink-soft);
  }
  .contact-lines {
    position: absolute; right: 40px; top: 150px;
    font-size: 12px; line-height: 1.5; text-align: right; color: var(--ink-soft);
  }
  .contact-lines .label { color: var(--gold); font-weight: 500; }
  .front-bands { position: absolute; left: 0; bottom: 0; width: 520px; height: 60px; }

  /* Back */
  .card-back {
    background: var(--card-dark); color: var(--light);
    display: flex; flex-direction: column; align-items: center;
  }
  .card-back .brand { margin-top: 92px; display: flex; align-items: center; gap: 12px; }
  .card-back .brand-name { color: var(--light); font-size: 28px; }
  .tagline { margin-top: 62px; text-align: center; font-size: 15px; letter-spacing: 0.5px; line-height: 1.35; }
  .tagline-services { color: var(--light); text-transform: uppercase; }
  .tagline-sectors { color: var(--gold); text-transform: uppercase; }
</style>
</head>
<body>
  <section class="card card-front">
    <div class="brand">
      <span class="brand-mark"></span>
      <span class="brand-name">Marlowe Building Co</span>
    </div>
    <p class="contact-address">42 Harbour Lane<br>Seacliff, WA 6031</p>
    <p class="contact-lines">
      <span class="label">Tel:</span> 08 9411 2087 · <span class="label">Mob:</span> 0412 558 201<br>
      <span class="label">Email:</span> marlowebuildingco@mailbox.com
    </p>
    <div class="person">
      <p class="person-name">ADA PETRESCU</p>
      <p class="person-role">Director</p>
    </div>
    <svg class="front-bands" viewBox="0 0 520 60" aria-hidden="true">
      <polygon points="0,46 330,46 330,60 0,60" fill="var(--gold)"/>
      <polygon points="340,22 520,22 520,60 330,60" fill="var(--ink)"/>
    </svg>
  </section>

  <section class="card card-back">
    <div class="brand">
      <span class="brand-mark"></span>
      <span class="brand-name">Marlowe Building Co</span>
    </div>
    <div class="tagline">
      <p class="tagline-services">New Homes - Additions and Renovations</p>
      <p class="tagline-sectors">Domestic &amp; Commercial Builders</p>
    </div>
  </section>
</body>
</html>
```